RT Website Home Page Design

The task is to develop a winning design for a replacement website for our client RT Plumbing, Heating, AC & Remodeling. ct

```html
<!DOCTYPE html>
<html lang="en">
<head>
<meta charset="utf-8">
<title>RT Plumbing, Heating, AC &amp; Remodeling</title>
<link rel="stylesheet" href="https://fonts.googleapis.com/css2?family=Baloo+2:wght@800&family=Outfit:wght@400;500;600&family=Poppins:wght@400;500;600;700&display=swap">
<style>
:root{
  --navy:#1f2a5a;
  --navy-deep:#1b2550;
  --yellow:#f6dc4c;
  --ink:#1d1d1f;
  --muted:#4a4a4a;
  --line:#9a9a9a;
  --teal:#1f8c98;
  --teal-dark:#146a75;
  --dark:#2b2b2e;
  --white:#ffffff;
}
*{box-sizing:border-box;margin:0;padding:0}
html,body{width:1200px;height:4850px;overflow:hidden}
body{position:relative;background:var(--white);font-family:"Poppins",sans-serif;color:var(--ink)}
.abs{position:absolute}
.heading{font-family:"Outfit",sans-serif;font-weight:500;color:var(--ink)}

/* header */
.site-header{top:0;left:0;width:1200px;height:83px;background:var(--white)}
.brand{left:58px;top:16px;display:flex;align-items:center;gap:10px}
.brand-mark{width:34px;height:34px;border-radius:50%;background:var(--navy)}
.brand-name{font-family:"Poppins",sans-serif;font-weight:700;font-size:17px;color:var(--navy);line-height:1.1}
.brand-name small{display:block;font-size:10px;font-weight:600}
.service-area{left:392px;top:30px;font-size:14px;color:var(--navy)}
.phone-pill{top:21px;height:40px;width:172px;background:var(--yellow);border-radius:8px;display:flex;align-items:center;gap:8px;padding-left:10px}
.phone-pill .num{font-family:"Outfit",sans-serif;font-weight:600;font-size:18px;color:var(--navy);line-height:1}
.phone-pill .num small{display:block;font-size:10px;font-weight:500;text-align:center}
.main-nav{top:83px;left:0;width:1200px;height:34px;background:var(--navy);display:flex;justify-content:space-between;align-items:center;padding:0 62px}
.main-nav a{color:var(--white);font-size:10.5px;font-weight:500;text-decoration:none;letter-spacing:.2px}

/* hero */
.hero{top:117px;left:0;width:1200px;height:627px;background:linear-gradient(120deg,#6b6a5c,#8a7f6c 45%,#5c6a6e);overflow:hidden}
.hero-shade{inset:0;background:rgba(25,30,45,.35)}
.hero-title{top:140px;left:0;width:1200px;text-align:center;font-family:"Baloo 2",sans-serif;font-weight:800;font-size:60px;line-height:78px;color:var(--white);letter-spacing:3px;text-transform:uppercase}
.hero-cta{top:313px;left:382px;width:434px;height:58px;background:var(--yellow);border-radius:30px;display:flex;align-items:center;justify-content:center;font-family:"Outfit",sans-serif;font-weight:600;font-size:24px;color:var(--navy);box-shadow:0 3px 6px rgba(0,0,0,.3)}
.hero-curve{left:0;bottom:0;width:1200px;height:80px}

/* services */
.intro-title{top:784px;left:0;width:1200px;text-align:center;font-size:32px}
.intro-text{top:842px;left:155px;width:890px;text-align:center;font-size:13px;line-height:22px;color:var(--muted)}
.service-grid{top:965px;left:209px;width:840px;height:420px;display:grid;grid-template-columns:repeat(4,210px);grid-template-rows:repeat(2,210px)}
.service{display:flex;flex-direction:column;align-items:center;justify-content:center;gap:18px;font-size:15px;text-align:center;line-height:20px;border-color:var(--line);border-style:solid;border-width:0}
.service:nth-child(-n+4){border-bottom-width:1px}
.service:not(:nth-child(4n)){border-right-width:1px}
.service-icon{width:60px;height:60px}

/* ready */
.ready-title{top:1450px;left:57px;font-size:35px;line-height:42px}
.ready-text{top:1558px;left:57px;width:490px;font-size:13px;line-height:22px;color:var(--muted)}
.ready-list{top:1650px;left:57px;list-style:none;font-size:13px;color:var(--muted)}
.ready-list li{display:flex;align-items:center;gap:8px;height:32px}
.btn-yellow{background:var(--yellow);font-family:"Poppins",sans-serif;font-weight:700;color:var(--navy);display:flex;align-items:center;justify-content:center;border-radius:6px;letter-spacing:.5px}
.ready-btn{top:1821px;left:57px;width:168px;height:36px;font-size:13px}
.ready-photo{top:1460px;left:675px;width:472px;height:440px;border-radius:12px;background:linear-gradient(160deg,#c9d6e3,#7f93ab 50%,#3c4b72)}
.trust-badge{top:1730px;left:624px;width:228px;height:78px;background:var(--navy);border-radius:10px 10px 10px 0;display:flex;align-items:center;gap:12px;padding-left:16px;color:var(--white)}
.trust-badge .dot{width:44px;height:44px;border-radius:50%;background:var(--yellow)}
.trust-badge strong{display:block;font-family:"Outfit",sans-serif;font-weight:500;font-size:38px;line-height:38px}
.trust-badge span{font-size:14px}

/* reminder */
.reminder{top:1975px;left:0;width:1200px;height:682px;background:linear-gradient(135deg,#3a3a3d,#242427 60%,#2e2e31)}
.reminder-photo{top:122px;left:53px;width:473px;height:439px;border-radius:12px;background:linear-gradient(135deg,#e6e1d8,#cfc7b9 55%,#8c8170)}
.reminder-copy{left:646px;width:500px;color:var(--white)}
.reminder-copy h2{font-family:"Outfit",sans-serif;font-weight:500;font-size:34px;line-height:40px;margin-bottom:8px}
.reminder-copy p{font-size:13px;line-height:22.5px;color:#e6e6e6}
.reminder-btn{top:503px;left:650px;width:170px;height:36px;font-size:13px}

/* savings */
.savings-title{top:2722px;left:0;width:1200px;text-align:center;font-size:34px;color:var(--navy)}
.offer{top:2826px;width:300px;text-align:center}
.offer-badge{width:240px;height:245px;margin:0 auto;position:relative}
.offer-badge .label{position:absolute;inset:0;display:flex;flex-direction:column;align-items:center;justify-content:center;font-family:"Outfit",sans-serif;font-weight:600;color:var(--yellow);font-size:40px;line-height:44px;transform:rotate(-12deg)}
.offer h3{font-family:"Outfit",sans-serif;font-weight:400;font-size:27px;color:var(--navy);margin-top:28px}
.offer p{font-size:13px;line-height:18px;color:var(--muted);margin:10px auto 0;width:250px;height:38px}
.offer-btn{width:172px;height:38px;margin:4px auto 0;background:var(--navy);color:var(--white);border-radius:19px;display:flex;align-items:center;justify-content:center;font-size:14px;font-weight:500}

/* form */
.quote{top:3291px;left:0;width:1200px;height:590px;background:linear-gradient(120deg,#3d4b78,#2b3866 60%,#34426f)}
.quote-shade{inset:0;background:rgba(31,42,90,.55)}
.field{height:36px;background:var(--white);font-size:12px;color:#333;padding:11px 14px}
.quote-btn{top:402px;left:516px;width:168px;height:38px;font-size:14px;font-weight:600;border-radius:7px}

/* blog */
.blog-title{top:3945px;left:0;width:1200px;text-align:center;font-size:34px;color:var(--navy)}
.post{top:4041px;width:348px}
.post-photo{height:211px}
.post-date{position:absolute;top:201px;left:18px;background:var(--yellow);font-size:11px;padding:3px 9px;color:var(--ink)}
.post h3{font-family:"Outfit",sans-serif;font-weight:500;font-size:19px;color:var(--navy);margin:20px 0 0 14px}
.post p{font-size:13px;line-height:19px;color:var(--muted);margin:8px 14px 0}
.post a{display:block;font-size:13px;color:#d08b2c;margin:12px 14px 0;text-decoration:none}

/* footer */
.site-footer{top:4469px;left:0;width:1200px;height:381px;background:var(--navy);color:var(--white)}
.footer-brand{top:68px;left:62px;display:flex;align-items:center;gap:10px}
.footer-brand .brand-mark{background:var(--yellow)}
.footer-brand .brand-name{color:var(--white)}
.copyright{top:213px;left:57px;font-size:13px;line-height:23px}
.footer-head{font-family:"Outfit",sans-serif;font-weight:500;font-size:22px;color:var(--yellow);letter-spacing:.5px}
.quick-links{top:80px;left:466px;list-style:none;font-size:14px;line-height:34px}
.contact-list{left:886px;font-size:13.5px;line-height:21px}
.contact-row{display:flex;gap:8px;align-items:flex-start}
.social-box{width:38px;height:38px;background:#3b63c4;border-radius:4px}
.card-chip{width:44px;height:28px;border-radius:3px;background:#e8ecf5}
</style>
</head>
<body>

<header class="site-header abs">
  <div class="brand abs">
    <div class="brand-mark"></div>
    <div class="brand-name">RT PLUMBING<small>HEATING, AC &amp; REMODELING</small></div>
  </div>
  <div class="service-area abs">Serving Millbrook, MA &amp; Neighboring Communities</div>
  <div class="phone-pill abs" style="left:786px">
    <svg width="24" height="24" viewBox="0 0 24 24"><circle cx="12" cy="12" r="11" fill="var(--navy)"/><path d="M8.5 6.5l2 2-1.2 1.6a7 7 0 0 0 4.6 4.6l1.6-1.2 2 2-1.5 2C11 17.5 6.5 13 6.5 8z" fill="#fff"/></svg>
    <div class="num">555.210.4830<small>(Request Service)</small></div>
  </div>
  <div class="phone-pill abs" style="left:975px">
    <svg width="24" height="24" viewBox="0 0 24 24"><circle cx="12" cy="12" r="11" fill="var(--navy)"/><path d="M8.5 6.5l2 2-1.2 1.6a7 7 0 0 0 4.6 4.6l1.6-1.2 2 2-1.5 2C11 17.5 6.5 13 6.5 8z" fill="#fff"/></svg>
    <div class="num">800.555.0172<small>(Request Quote)</small></div>
  </div>
</header>

<nav class="main-nav abs">
  <a>ABOUT</a><a>PLUMBING</a><a>WATER HEATERS</a><a>HEATING</a><a>AIR CONDITIONING</a><a>INDOOR AIR QUALITY</a><a>COMMERCIAL</a><a>HANDY WORK &amp; REMODELING</a><a>CONTACT</a>
</nav>

<section class="hero abs" role="img" aria-label="Photo of a smiling technician with a clipboard talking with a homeowner in a bright kitchen">
  <div class="hero-shade abs"></div>
  <h1 class="hero-title abs">Enjoy the best of home<br>living. Indoors &amp; out</h1>
  <div class="hero-cta abs">CONTACT US TO GET STARTED</div>
  <svg class="hero-curve abs" viewBox="0 0 1200 80" preserveAspectRatio="none">
    <path d="M0 35 Q600 -20 1200 40 L1200 80 L0 80Z" fill="var(--yellow)"/>
    <path d="M0 60 Q600 0 1200 58 L1200 80 L0 80Z" fill="#fff"/>
  </svg>
</section>

<h2 class="intro-title heading abs">More of What You Need</h2>
<p class="intro-text abs">In its formative years, RT Plumbing, Heating &amp; Air was focused primarily on heating and plumbing. Since joining forces with Brookline Home Services, we've expanded into air conditioning, drain cleaning, improved indoor air quality, and a wide range of handyman and remodeling services.</p>

<div class="service-grid abs">
  <div class="service"><svg class="service-icon" viewBox="0 0 60 60"><rect x="8" y="14" width="32" height="10" rx="2" fill="#111"/><rect x="22" y="6" width="6" height="10" fill="#111"/><rect x="14" y="4" width="22" height="4" rx="2" fill="#111"/><rect x="34" y="20" width="8" height="14" fill="#111"/><path d="M38 40c-3 5-3 8 0 8s3-3 0-8z" fill="#111"/></svg>Plumbing</div>
  <div class="service"><svg class="service-icon" viewBox="0 0 60 60"><rect x="8" y="16" width="44" height="28" rx="14" fill="none" stroke="#111" stroke-width="3"/><line x1="30" y1="22" x2="48" y2="22" stroke="#111" stroke-width="3"/><line x1="30" y1="38" x2="48" y2="38" stroke="#111" stroke-width="3"/><circle cx="21" cy="30" r="6" fill="#111"/></svg>WaterHeaters</div>
  <div class="service"><svg class="service-icon" viewBox="0 0 60 60"><rect x="10" y="24" width="40" height="22" fill="none" stroke="#111" stroke-width="3"/><g stroke="#111" stroke-width="3"><line x1="18" y1="24" x2="18" y2="46"/><line x1="26" y1="24" x2="26" y2="46"/><line x1="34" y1="24" x2="34" y2="46"/><line x1="42" y1="24" x2="42" y2="46"/></g><path d="M22 10q3 4 0 8M30 10q3 4 0 8M38 10q3 4 0 8" fill="none" stroke="#111" stroke-width="2"/></svg>Heating</div>
  <div class="service"><svg class="service-icon" viewBox="0 0 60 60"><circle cx="30" cy="30" r="13" fill="none" stroke="#111" stroke-width="4"/><g stroke="#111" stroke-width="4"><line x1="30" y1="6" x2="30" y2="14"/><line x1="30" y1="46" x2="30" y2="54"/><line x1="6" y1="30" x2="14" y2="30"/><line x1="46" y1="30" x2="54" y2="30"/><line x1="13" y1="13" x2="19" y2="19"/><line x1="41" y1="41" x2="47" y2="47"/><line x1="47" y1="13" x2="41" y2="19"/><line x1="19" y1="41" x2="13" y2="47"/></g></svg>Air Conditioning</div>
  <div class="service"><svg class="service-icon" viewBox="0 0 60 60"><g fill="none" stroke="#111" stroke-width="3" stroke-linecap="round"><path d="M8 22h30a6 6 0 1 0-6-6"/><path d="M8 32h38a6 6 0 1 1-6 6"/><path d="M8 42h22"/></g></svg>Indoor Air Quality</div>
  <div class="service"><svg class="service-icon" viewBox="0 0 60 60"><rect x="8" y="8" width="44" height="44" rx="5" fill="none" stroke="#111" stroke-width="3"/><rect x="14" y="14" width="32" height="8" fill="#111"/><g fill="#111"><circle cx="20" cy="36" r="3"/><circle cx="30" cy="36" r="3"/><circle cx="40" cy="36" r="3"/></g></svg>Water Filtration</div>
  <div class="service"><svg class="service-icon" viewBox="0 0 60 60"><circle cx="30" cy="30" r="18" fill="none" stroke="#111" stroke-width="8" stroke-dasharray="7 4"/><circle cx="30" cy="30" r="7" fill="#111"/></svg>Remodeling &amp;<br>Handy Work</div>
  <div class="service"><svg class="service-icon" viewBox="0 0 60 60"><rect x="8" y="8" width="44" height="8" fill="#111"/><rect x="12" y="16" width="36" height="34" fill="none" stroke="#111" stroke-width="4"/><path d="M30 26c-5 6-6 10-2 14h4c4-4 3-8-2-14z" fill="#111"/></svg>Gas Fireplaces</div>
</div>

<h2 class="ready-title heading abs">We're Ready When<br>Your Need Us</h2>
<p class="ready-text abs">Our network of service professionals and dispatch team can handle a high volume of projects while providing top-class service whenever you need us.</p>
<ul class="ready-list abs">
  <li><svg width="16" height="16" viewBox="0 0 16 16"><circle cx="8" cy="8" r="6.5" fill="none" stroke="#222" stroke-width="1.5"/><path d="M4.5 8l2.5 2.5 5-5" fill="none" stroke="#222" stroke-width="1.8"/></svg>60 Evployees to care for your maintenance deeds</li>
  <li><svg width="16" height="16" viewBox="0 0 16 16"><circle cx="8" cy="8" r="6.5" fill="none" stroke="#222" stroke-width="1.5"/><path d="M4.5 8l2.5 2.5 5-5" fill="none" stroke="#222" stroke-width="1.8"/></svg>30 Virtual Assistants ready to help when you call</li>
  <li><svg width="16" height="16" viewBox="0 0 16 16"><circle cx="8" cy="8" r="6.5" fill="none" stroke="#222" stroke-width="1.5"/><path d="M4.5 8l2.5 2.5 5-5" fill="none" stroke="#222" stroke-width="1.8"/></svg>90 Techicians ready to go</li>
  <li><svg width="16" height="16" viewBox="0 0 16 16"><circle cx="8" cy="8" r="6.5" fill="none" stroke="#222" stroke-width="1.5"/><path d="M4.5 8l2.5 2.5 5-5" fill="none" stroke="#222" stroke-width="1.8"/></svg>No Runaround - Let's get to work!</li>
</ul>
<div class="ready-btn btn-yellow abs">SET UP A CALL</div>
<div class="ready-photo abs" role="img" aria-label="Photo of two smiling technicians in work uniforms and tool belts standing in front of a white service van"></div>
<div class="trust-badge abs"><div class="dot"></div><div><strong>2000+</strong><span>Customer Trusted</span></div></div>

<section class="reminder abs" role="img" aria-label="Dark blurred kitchen backdrop">
  <div class="reminder-photo abs" role="img" aria-label="Photo of a woman relaxing on a sofa beneath a wall-mounted air conditioner"></div>
  <div class="reminder-copy abs" style="top:120px">
    <h2>Back to School Reminder</h2>
    <p>Most families see an uptick in morning "rush hour" activity once the school year begins, and so does your water heater. Can yours keep up with the increased demand? Contact us today for a water heater check-up and free quote on a replacement system.</p>
  </div>
  <div class="reminder-copy abs" style="top:295px">
    <h2>The RT Difference Makers</h2>
    <p>RT is a favorite choice among homeowners who appreciate our extensive range of home comfort and related services. Others like us best for our 100% satisfaction guarantee, while still others enjoy the many benefits that membership in our Preferred Service Club provides. Add it all up, and there's a lot to like about RT Plumbing, Heating, AC &amp; Remodeling.</p>
  </div>
  <div class="reminder-btn btn-yellow abs">LEARN MORE</div>
</section>

<h2 class="savings-title heading abs">Enjoy the Savings...Plus the Added Comfort!</h2>
<div class="offer abs" style="left:84px">
  <div class="offer-badge" role="img" aria-label="Teal savings badge: Save $120"><svg width="240" height="245" viewBox="0 0 240 245"><circle cx="122" cy="122" r="118" fill="var(--teal-dark)"/><circle cx="116" cy="128" r="108" fill="var(--teal)"/></svg><div class="label">Save<br>$120</div></div>
  <h3>New Water Heater</h3>
  <p>on a new water heater, tank-style or tankless.</p>
  <div class="offer-btn">Click for details</div>
</div>
<div class="offer abs" style="left:449px">
  <div class="offer-badge" role="img" aria-label="Teal savings badge: Save $350"><svg width="240" height="245" viewBox="0 0 240 245"><circle cx="122" cy="122" r="118" fill="var(--teal-dark)"/><circle cx="116" cy="128" r="108" fill="var(--teal)"/></svg><div class="label">Save<br>$350</div></div>
  <h3>HVAC System</h3>
  <p>on a new heating or cooling system.</p>
  <div class="offer-btn">Click for details</div>
</div>
<div class="offer abs" style="left:815px">
  <div class="offer-badge" role="img" aria-label="Teal savings badge: Save $35"><svg width="240" height="245" viewBox="0 0 240 245"><circle cx="122" cy="122" r="118" fill="var(--teal-dark)"/><circle cx="116" cy="128" r="108" fill="var(--teal)"/></svg><div class="label">Save<br>$35</div></div>
  <h3>First-time Customer</h3>
  <p>on any service we provide.</p>
  <div class="offer-btn">Click for details</div>
</div>

<section class="quote abs" role="img" aria-label="Photo of a plumber working under a sink, overlaid in navy">
  <div class="quote-shade abs"></div>
  <div class="field abs" style="top:132px;left:177px;width:413px">*Name</div>
  <div class="field abs" style="top:132px;left:609px;width:412px">Phone</div>
  <div class="field abs" style="top:184px;left:177px;width:413px">Address</div>
  <div class="field abs" style="top:184px;left:609px;width:412px">City</div>
  <div class="field abs" style="top:235px;left:177px;width:413px">Zip</div>
  <div class="field abs" style="top:235px;left:609px;width:412px">*Email</div>
  <div class="field abs" style="top:285px;left:177px;width:844px;height:98px">Comments</div>
  <div class="quote-btn btn-yellow abs">LEARN MORE</div>
</section>

<h2 class="blog-title heading abs">Latest Blog Feeds</h2>
<article class="post abs" style="left:53px">
  <div class="post-photo" role="img" aria-label="Photo of a woman cheering in a living room under an air conditioner" style="background:linear-gradient(135deg,#eee7dc,#c8b79e)"></div>
  <span class="post-date">30May 2023</span>
  <h3>Blog title here.....</h3>
  <p>Lorem ipsum dolor sit amet, consectetur adipiscing elit, sed do eiusmod tempor incidid unt ut labore et dolore magna aliqua.</p>
  <a>Read more.....</a>
</article>
<article class="post abs" style="left:426px">
  <div class="post-photo" role="img" aria-label="Photo of a technician shaking hands with a couple next to a furnace" style="background:linear-gradient(135deg,#d8d2c8,#7d7468)"></div>
  <span class="post-date">30May 2023</span>
  <h3>Blog title here.....</h3>
  <p>Lorem ipsum dolor sit amet, consectetur adipiscing elit, sed do eiusmod tempor incidid unt ut labore et dolore magna aliqua.</p>
  <a>Read more.....</a>
</article>
<article class="post abs" style="left:799px">
  <div class="post-photo" role="img" aria-label="Photo of a hand holding a smartphone with a thermostat app" style="background:linear-gradient(135deg,#e4d2bf,#a07f63)"></div>
  <span class="post-date">30May 2023</span>
  <h3>Blog title here.....</h3>
  <p>Lorem ipsum dolor sit amet, consectetur adipiscing elit, sed do eiusmod tempor incidid unt ut labore et dolore magna aliqua.</p>
  <a>Read more.....</a>
</article>

<footer class="site-footer abs">
  <div class="footer-brand abs">
    <div class="brand-mark"></div>
    <div class="brand-name">RT PLUMBING<small>HEATING, AC &amp; REMODELING</small></div>
  </div>
  <p class="copyright abs">@ 2023 RT Heating &amp; Plumbing,<br>All Rights Reserved.</p>

  <h4 class="footer-head abs" style="top:36px;left:466px">QUICK LINK</h4>
  <ul class="quick-links abs">
    <li>- About</li><li>- Plumbing</li><li>- Water Heaters</li><li>- Heating</li><li>- Air Conditioning</li><li>- Indoor Air Quality</li><li>- Commercial</li><li>- Handy Work &amp; Remodeling</li>
  </ul>

  <h4 class="footer-head abs" style="top:36px;left:886px">CONTAC US</h4>
  <div class="contact-list abs" style="top:86px">
    <div class="contact-row"><svg width="16" height="20" viewBox="0 0 16 20"><path d="M8 1a6 6 0 0 0-6 6c0 5 6 12 6 12s6-7 6-12a6 6 0 0 0-6-6z" fill="var(--yellow)"/><circle cx="8" cy="7" r="2.3" fill="var(--navy)"/></svg><span>118 Maple Street<br>Oakdale, MA 01990</span></div>
    <div class="contact-row" style="margin-top:20px"><svg width="16" height="16" viewBox="0 0 24 24"><path d="M6 3l4 4-2 3a11 11 0 0 0 6 6l3-2 4 4-3 3C10 21 3 14 3 6z" fill="var(--yellow)"/></svg><span>555.210.4830 ( Request Service )</span></div>
    <div class="contact-row" style="margin-top:14px"><svg width="16" height="16" viewBox="0 0 24 24"><path d="M6 3l4 4-2 3a11 11 0 0 0 6 6l3-2 4 4-3 3C10 21 3 14 3 6z" fill="var(--yellow)"/></svg><span>800.555.0172 ( Request a Quote )</span></div>
    <div class="contact-row" style="margin-top:20px;align-items:center"><span style="font-weight:600">FOLLOW US :</span><div class="social-box"></div></div>
    <div class="contact-row" style="margin-top:28px;gap:6px"><div class="card-chip"></div><div class="card-chip"></div><div class="card-chip"></div><div class="card-chip"></div></div>
  </div>
</footer>

</body>
</html>
```